Bus Bench Ad Design Needed

Hi there. We would like to design an eye catching bus bench ad! The information that we would like to have on it is found below:

- Our logo which is attached below. We would this to take up at least half of the bus bench.
- Our phone number in bold, very visible to see. 555-318-2694. White numbers on an eye catching colored background.
- Our web address : www.SplitEase472.example
- A "Ring Otto" phrase in a black circle with yellow bold letters. Want the "Ring Otto" to be somewhat angled. We are thinking that the "Ring Otto" should be directly below the image in our logo.
- Our tag line we want somewhere in here as well which is "Divorce made easy - at a price you'll like!"

```html
<!DOCTYPE html>
<html lang="en">
<head>
<meta charset="utf-8">
<title>SplitEase Bench Ad</title>
<link rel="stylesheet" href="https://fonts.googleapis.com/css2?family=Anton&family=Open+Sans:wght@400;700&display=swap">
<style>
  :root {
    --page: #e4e4e4;
    --brand-blue: #0a80c6;
    --ink: #2e2e2e;
    --black: #0b0b0b;
    --white: #ffffff;
    --yellow: #fff200;
    --wood-dark: #3d2618;
    --wood-mid: #6b4630;
  }
  html, body {
    margin: 0;
    width: 1200px;
    height: 1200px;
    overflow: hidden;
    background: var(--page);
  }
  .bench-ad {
    position: absolute;
    left: 30px;
    top: 381px;
    width: 1140px;
    height: 438px;
  }
  .bench-ad svg { display: block; width: 100%; height: 100%; }
  .headline { font-family: "Anton", Impact, sans-serif; }
  .body-text { font-family: "Open Sans", Arial, sans-serif; }
</style>
</head>
<body>
<div class="bench-ad">
  <svg viewBox="0 0 1524 585" xmlns="http://www.w3.org/2000/svg">
    <defs>
      <linearGradient id="panelWhite" x1="0" y1="0" x2="1" y2="1">
        <stop offset="0" stop-color="#ffffff"/>
        <stop offset="1" stop-color="#e9e9e9"/>
      </linearGradient>
      <linearGradient id="woodTone" x1="0" y1="0" x2="1" y2="1">
        <stop offset="0" stop-color="var(--wood-dark)"/>
        <stop offset="0.5" stop-color="var(--wood-mid)"/>
        <stop offset="1" stop-color="var(--wood-dark)"/>
      </linearGradient>
      <radialGradient id="badgeFill" cx="0.5" cy="0.2" r="0.8">
        <stop offset="0" stop-color="#d9d9d9"/>
        <stop offset="0.45" stop-color="#3a3a3a"/>
        <stop offset="0.7" stop-color="#000000"/>
      </radialGradient>
    </defs>

    <!-- panel base -->
    <rect class="panel" width="1524" height="585" fill="url(#panelWhite)"/>

    <!-- blue curved band with silver edge -->
    <path class="curve-band" d="M470 0 H580 Q690 270 555 585 H470 Z" fill="var(--brand-blue)"/>
    <path class="curve-edge" d="M580 0 H592 Q700 270 567 585 H555 Q690 270 580 0 Z" fill="#b8b8b8"/>

    <!-- photo area -->
    <path class="photo" role="img" aria-label="Top-down photo of hands signing a divorce certificate on a wooden table, with rings and a phone"
          d="M0 0 H480 Q600 300 480 585 H0 Z" fill="url(#woodTone)"/>

    <!-- brand name -->
    <text class="body-text brand-name" x="880" y="150" font-size="82" fill="var(--brand-blue)">SplitEase</text>
    <text class="body-text brand-sub" x="882" y="190" font-size="31" fill="var(--ink)">Non Lawyer Documents Service</text>

    <!-- tagline -->
    <text class="headline tagline" x="772" y="305" font-size="80" fill="var(--ink)"><tspan fill="var(--brand-blue)">Divorce</tspan> made easy</text>
    <text class="headline tagline" x="772" y="405" font-size="80" fill="var(--ink)">at a <tspan fill="var(--brand-blue)">price you'll like!</tspan></text>

    <!-- contact bar -->
    <polygon class="web-strip" points="545,475 1037,475 985,585 530,585" fill="var(--black)"/>
    <polygon class="phone-strip" points="1047,475 1524,475 1524,585 995,585" fill="var(--brand-blue)"/>

    <!-- globe icon -->
    <g class="icon-globe" fill="none" stroke="var(--white)" stroke-width="2">
      <circle cx="578" cy="531" r="24"/>
      <circle cx="578" cy="531" r="14" stroke="var(--brand-blue)"/>
      <ellipse cx="578" cy="531" rx="6" ry="14" stroke="var(--brand-blue)"/>
      <line x1="564" y1="531" x2="592" y2="531" stroke="var(--brand-blue)"/>
    </g>
    <text class="body-text web-address" x="620" y="541" font-size="27" fill="var(--white)">www.<tspan fill="var(--brand-blue)" font-weight="700">SplitEase472</tspan>.example</text>

    <!-- phone icon -->
    <path class="icon-phone" d="M1048 514 l8 -4 l7 11 l-5 4 q3 8 11 13 l5 -5 l11 7 l-4 8 q-18 2 -33 -34 z"
          fill="none" stroke="var(--white)" stroke-width="2" stroke-linejoin="round"/>
    <text class="body-text phone-number" x="1095" y="552" font-size="56" font-weight="700" fill="var(--white)">555-318-2694</text>

    <!-- call badge -->
    <g class="call-badge">
      <circle cx="588" cy="292" r="135" fill="var(--white)"/>
      <circle cx="588" cy="292" r="128" fill="var(--black)"/>
      <circle cx="588" cy="292" r="121" fill="url(#badgeFill)"/>
      <text class="headline" x="591" y="287" font-size="80" text-anchor="middle" fill="#222">RING</text>
      <text class="headline" x="588" y="284" font-size="80" text-anchor="middle" fill="var(--yellow)">RING</text>
      <text class="headline" x="591" y="366" font-size="80" text-anchor="middle" fill="#222">OTTO</text>
      <text class="headline" x="588" y="363" font-size="80" text-anchor="middle" fill="var(--yellow)">OTTO</text>
    </g>
  </svg>
</div>
</body>
</html>
```